Web Design Project for velbrook

We are looking for a sleek and sophisticated website design for our already developed web-based gallery management software application. Here is a link to our web-app: http://www.vel-brook.co

You will login on the main page and then we would like to include all of the information on the PDF that I am providing below (it outlines what?, where?, why? who? and how much?). Basically, we need a home page, about page, and a pricing page, as well as a sign up page that should be navigable from the upper right hand corner of the site where the sign in/sign up would be located. Also, our 3 tenets are that the software program is "attractive, accessible, and affordable", which might need to be somehow incorporated. There are a few websites that we would like for you to take inspiration from listed below:

https://tidemoxen.com (for homepage)
https://plumwovenly.com (for homepage/pricing page/etc)
https://tidemoxen.com/tour (for a tour of how the product works)

We are currently having a logo designed and will share that as soon as it is available! Also, let us know if you need photos/screen shots, as we can provide them.

Thanks!

Reason: Extending deadline as we are just now getting designs we would like to see fully developed.

Target Market(s)

art galleries, artists, art collectors, art consultants, museums

Industry/Entity Type

Software

Requirements
Must have
• Home page
About page (or tour through the app)
Pricing page
Sign up page (the more click-throughs to signing up the better)

```html
<!DOCTYPE html>
<html lang="en">
<head>
<meta charset="utf-8">
<title>velbrook — Pricing</title>
<link href="https://fonts.googleapis.com/css2?family=Comfortaa:wght@300;400&family=Noto+Sans:wght@400&display=swap" rel="stylesheet">
<style>
  :root {
    --brand: #3bbfe0;
    --ink: #222222;
    --page: #f2f2f2;
    --footer: #2b2b2b;
    --footer-text: #e8e8e8;
    --orange: #f57c00;
    --link: #1a9fd0;
    --card: rgba(255,255,255,0.72);
    --title-box: #2a2a2a;
  }
  * { box-sizing: border-box; margin: 0; padding: 0; }
  html, body { width: 823px; height: 1200px; overflow: hidden; }
  body { position: relative; background: var(--page); font-family: Arial, Helvetica, sans-serif; color: var(--ink); }

  .site-header { position: absolute; top: 0; left: 0; width: 823px; height: 61px; background: #fff; }
  .brand { position: absolute; left: 20px; top: 12px; display: flex; align-items: center; gap: 8px; }
  .brand-dot { width: 34px; height: 34px; border: 4px solid var(--brand); border-radius: 50%; }
  .brand-name { font-family: "Comfortaa", sans-serif; font-weight: 300; font-size: 26px; color: var(--brand); }
  .main-nav { position: absolute; right: 10px; top: 16px; display: flex; gap: 22px; align-items: center; font-family: "Noto Sans", sans-serif; font-size: 20px; }
  .main-nav a { color: var(--ink); text-decoration: none; }
  .main-nav .nav-signup { background: var(--brand); color: #fff; padding: 2px 8px; border-radius: 3px; }

  .hero { position: absolute; top: 61px; left: 0; width: 823px; height: 450px;
    background: radial-gradient(ellipse at 55% 45%, #b8a88a 0%, #6e5c45 45%, #2a221a 100%); }
  .step-card { position: absolute; top: 95px; width: 253px; height: 239px; background: var(--card); border-radius: 8px; padding: 18px 10px 0 20px; }
  .step-title { font-family: "Comfortaa", sans-serif; font-weight: 300; font-size: 40px; color: #222; line-height: 1; margin-bottom: 20px; white-space: nowrap; }
  .step-text { font-family: "Noto Sans", sans-serif; font-size: 20px; line-height: 26px; letter-spacing: 1.2px; color: #222; white-space: nowrap; }

  .section-title { position: absolute; left: 170px; top: 491px; width: 483px; height: 78px; background: var(--title-box); border-radius: 4px;
    color: #fff; font-family: "Comfortaa", sans-serif; font-weight: 300; font-size: 33px; display: flex; align-items: center; justify-content: center; white-space: nowrap; }

  .pricing-copy { position: absolute; left: 17px; top: 601px; width: 785px; font-size: 16.8px; line-height: 22.6px; }
  .btn-signup { position: absolute; left: 33px; top: 718px; width: 200px; height: 36px; background: var(--orange); color: #fff;
    font-family: "Noto Sans", sans-serif; font-size: 24px; display: flex; align-items: center; justify-content: center; text-decoration: none; }
  .help-copy { position: absolute; left: 15px; top: 778px; width: 790px; font-size: 19px; line-height: 26px; }
  .help-copy a { color: var(--link); text-decoration: none; }

  .site-footer { position: absolute; top: 935px; left: 0; width: 823px; height: 265px; background: var(--footer); border-top: 2px solid #555;
    font-family: "Comfortaa", sans-serif; color: var(--footer-text); }
  .footer-nav { position: absolute; left: 36px; top: 51px; list-style: none; font-size: 18px; line-height: 27.5px; }
  .footer-contact { position: absolute; left: 295px; top: 49px; font-size: 17px; }
  .footer-contact p { margin-bottom: 11px; line-height: 23px; }
  .footer-contact .contact-large { font-size: 19px; }
  .social { position: absolute; top: 67px; width: 48px; height: 48px; border-radius: 50%; background: var(--brand); }
  .social-a { left: 595px; }
  .social-b { left: 670px; }
  .copyright { position: absolute; left: 38px; top: 240px; font-size: 15px; }
</style>
</head>
<body>
  <header class="site-header">
    <div class="brand"><span class="brand-dot"></span><span class="brand-name">velbrook</span></div>
    <nav class="main-nav">
      <a href="#">Home</a><a href="#">About</a><a href="#">Pricing</a>
      <a href="#" class="nav-signup">Sign Up</a><a href="#">Log In</a>
    </nav>
  </header>

  <section class="hero" role="img" aria-label="Softly blurred photo of an art gallery interior with framed works on the walls">
    <div class="step-card" style="left:14px">
      <h2 class="step-title">Step 1:</h2>
      <p class="step-text">Contact our friendly<br>staff to determine<br>your velBROOK<br>needs.</p>
    </div>
    <div class="step-card" style="left:285px">
      <h2 class="step-title">Step 2:</h2>
      <p class="step-text">Actvate and<br>integrate your<br>velBROOK account.<br>Free for the first 60<br>days!</p>
    </div>
    <div class="step-card" style="left:555px">
      <h2 class="step-title">Step 3:</h2>
      <p class="step-text">Get FREE support,<br>updates, and work<br>with your sales<br>manger to grow<br>your business!</p>
    </div>
  </section>

  <h1 class="section-title">How Much is velBROOK?</h1>

  <p class="pricing-copy">velBROOK is one of the most affordable gallery database options on the marketplace with an initial activation fee of $500 and a modest monthly maintenance fee of $99. That’s it, and with that is included system set-up if using our import template, support, hosting, back-up and any upgrades to improve the system.</p>

  <a href="#" class="btn-signup">Sign Up Here</a>

  <p class="help-copy">Need help getting started? Want assistance uploading your client list, art inventory, or past sales? <a href="#">Email us here.</a></p>

  <footer class="site-footer">
    <ul class="footer-nav">
      <li>Home</li><li>About</li><li>Pricing</li><li>Sign Up</li><li>Log In</li>
    </ul>
    <div class="footer-contact">
      <p>Contact Us</p>
      <p>help@velbrook-mail.net</p>
      <p class="contact-large">(555) 310-2874</p>
      <p class="contact-large">48 Larkspur Row<br>Fenwick, OR<br>97031</p>
    </div>
    <span class="social social-a" aria-label="Social profile"></span>
    <span class="social social-b" aria-label="Social profile"></span>
    <p class="copyright">velBROOK 2013 - Sitemap</p>
  </footer>
</body>
</html>
```